Bookmark Design

We would like to design a book mark with logos of our two business and a quote.

One side with the quote "The first wealth is health" - Tobias Quill Harrow and the two logos.

The back side has the two logos with its respective phone numbers and a common address (this is to be advised to the winner of the project).

```html
<!DOCTYPE html>
<html lang="en">
<head>
<meta charset="utf-8">
<title>Bookmark – Harbourline Dental &amp; Maplecourt Clinic</title>
<link rel="stylesheet" href="https://fonts.googleapis.com/css2?family=Arimo:ital,wght@0,400;0,700;1,700&display=swap">
<style>
  :root{
    --canvas:#eef0f0;
    --green-light:#8dc63f;
    --green:#5fb55a;
    --green-dark:#3d9a48;
    --blue:#1f56a8;
    --white:#ffffff;
    --ink:#222222;
    --mist:#e9f4e6;
    --line:#d6dad8;
  }
  *{margin:0;padding:0;box-sizing:border-box}
  html,body{width:835px;height:1200px;overflow:hidden;background:var(--canvas)}
  body{font-family:"Arimo",Arial,sans-serif;position:relative}

  .bookmark{position:absolute;top:42px;width:345px;height:1125px;border-radius:24px;overflow:hidden}
  .bookmark--front{left:56px;
    background:linear-gradient(180deg,var(--green-light) 0%,var(--green) 18%,var(--blue) 48%,var(--green) 75%,var(--green-light) 100%);}
  .bookmark--back{left:432px;border:1.5px solid var(--line);
    background:linear-gradient(180deg,var(--white) 0%,var(--white) 55%,var(--mist) 78%,#cfe8c8 100%);}

  .deco{position:absolute;inset:0;width:100%;height:100%}

  .quote{position:absolute;left:0;right:0;top:270px;text-align:center;color:var(--white)}
  .quote__mark{font-family:Georgia,"Times New Roman",serif;font-weight:700;font-size:190px;line-height:1;height:130px;display:block}
  .quote__text{font-size:46px;line-height:1.18;margin-top:60px}
  .quote__author{font-size:15px;font-weight:700;font-style:italic;margin-top:110px}

  .brand{position:absolute;left:0;right:0;text-align:center}
  .brand__name{color:var(--green-dark);font-weight:700;font-size:32px;line-height:1.1}
  .brand__mark{width:100px;height:100px;border-radius:50%;background:var(--green-dark);margin:0 auto 16px}
  .brand--dental{top:100px}
  .brand--clinic{top:395px}

  .contact{position:absolute;left:0;right:0;display:flex;justify-content:center;align-items:center;gap:10px;color:var(--ink);font-size:20px}
  .contact svg{flex:none}
  .contact--dental{top:305px}
  .contact--clinic{top:560px}
  .contact--address{top:600px;font-size:18px}
</style>
</head>
<body>
  <section class="bookmark bookmark--front" aria-label="Bookmark front with quote">
    <svg class="deco" viewBox="0 0 345 1125" aria-hidden="true">
      <circle cx="300" cy="70" r="170" fill="#ffffff" fill-opacity="0.08"/>
      <circle cx="320" cy="40" r="90" fill="#ffffff" fill-opacity="0.06"/>
      <circle cx="250" cy="1130" r="230" fill="#ffffff" fill-opacity="0.10"/>
      <circle cx="240" cy="1140" r="150" fill="#ffffff" fill-opacity="0.08"/>
    </svg>
    <blockquote class="quote">
      <span class="quote__mark">“</span>
      <p class="quote__text">The<br>first<br>wealth is<br>Health</p>
      <p class="quote__author">-Tobias Quill Harrow</p>
    </blockquote>
  </section>

  <section class="bookmark bookmark--back" aria-label="Bookmark back with contacts">
    <svg class="deco" viewBox="0 0 345 1125" aria-hidden="true">
      <circle cx="300" cy="1030" r="250" fill="#9fd08e" fill-opacity="0.35"/>
      <circle cx="260" cy="1120" r="200" fill="#6fbf5f" fill-opacity="0.55"/>
    </svg>

    <div class="brand brand--dental">
      <p class="brand__name">Harbourline<br>Dental</p>
    </div>
    <p class="contact contact--dental">
      <svg width="24" height="24" viewBox="0 0 24 24" aria-hidden="true"><circle cx="12" cy="12" r="12" fill="var(--green-dark)"/><path d="M8.2 6.5l2 2-1.2 1.5a7 7 0 0 0 5 5l1.5-1.2 2 2-1.5 1.7c-4.5 0-9.5-5-9.5-9.5z" fill="#fff"/></svg>
      +41 200 555 0
    </p>

    <div class="brand brand--clinic">
      <div class="brand__mark"></div>
      <p class="brand__name">Maplecourt Clinic</p>
    </div>
    <p class="contact contact--clinic">
      <svg width="24" height="24" viewBox="0 0 24 24" aria-hidden="true"><circle cx="12" cy="12" r="12" fill="var(--blue)"/><path d="M8.2 6.5l2 2-1.2 1.5a7 7 0 0 0 5 5l1.5-1.2 2 2-1.5 1.7c-4.5 0-9.5-5-9.5-9.5z" fill="#fff"/></svg>
      +41 200 555 0
    </p>
    <p class="contact contact--address">
      <svg width="20" height="20" viewBox="0 0 20 20" aria-hidden="true"><circle cx="10" cy="10" r="10" fill="var(--ink)"/><path d="M10 4a3.5 3.5 0 0 0-3.5 3.5c0 2.6 3.5 7 3.5 7s3.5-4.4 3.5-7A3.5 3.5 0 0 0 10 4zm0 4.8a1.3 1.3 0 1 1 0-2.6 1.3 1.3 0 0 1 0 2.6z" fill="#fff"/></svg>
      common address goes here
    </p>
  </section>
</body>
</html>
```